Brevant Business Card

I have a business that is called "Brevant Electrical Products LTD" My company deals with top of the range laptops and mobile phones that are exclusive. I need a business card that will be eye catching but not over complicated.

Target Market(s)

Adults aged 19 to 50
Upper middle class

Industry/Entity Type

Business

Requirements
Must have
• Company name/logo (file attached)
• It must have my contact information which is:

• Name: Dale Marwick

• Position: Managing Director 

• Business Address: 7 Hapton Row, London, W4 9QD

• Contact Number: 02085193604
• Mobile: 07814260537
• Email: info@brevant-goods.co.uk
Nice to have
• Simple and stylish
• Eye catching

```html
<!DOCTYPE html>
<html lang="en">
<head>
<meta charset="utf-8">
<title>Brevant Business Card Concepts</title>
<link rel="stylesheet" href="https://fonts.googleapis.com/css2?family=Lato:wght@400;700&display=swap">
<style>
  :root {
    --ink: #1b1f24;
    --grey: #5c6670;
    --brand: #1596c9;
    --brand-deep: #0a5fa8;
    --sky: #8fd4ee;
    --sky-pale: #dff3fb;
    --teal: #17a6c4;
    --rule: #c9ccd0;
    --paper: #ffffff;
  }
  * { margin: 0; padding: 0; box-sizing: border-box; }
  html, body { width: 1200px; height: 2274px; overflow: hidden; background: var(--paper); }
  body { position: relative; font-family: "Lato", Arial, sans-serif; color: var(--ink); }

  .card { position: absolute; left: 60px; width: 1085px; background: var(--paper); border: 2px solid var(--rule); overflow: hidden; }
  .card--laptop { top: 63px; height: 607px; }
  .card--waves { top: 870px; height: 762px; }
  .card--frame { top: 1675px; height: 572px; }

  .abs { position: absolute; white-space: nowrap; }
  .person-name { font-weight: 700; font-size: 38px; color: var(--ink); }
  .person-role { font-variant: small-caps; font-size: 30px; color: var(--ink); letter-spacing: 1px; }
  .company { font-weight: 700; font-size: 38px; color: var(--brand); }
  .detail { font-size: 28px; color: var(--grey); line-height: 34px; }
  .detail--caps { font-variant: small-caps; color: var(--ink); letter-spacing: 1px; }
  .brand-name { font-weight: 700; font-size: 64px; color: var(--brand); letter-spacing: 2px; }

  /* Card 1 */
  .card--laptop .accent-band { left: 0; top: 200px; width: 580px; height: 44px;
    background: linear-gradient(90deg, var(--sky) 0%, var(--sky-pale) 60%, rgba(255,255,255,0) 100%); }
  .card--laptop .edge-glow { left: 0; top: 260px; width: 70px; height: 347px;
    background: linear-gradient(90deg, var(--sky) 0%, rgba(255,255,255,0) 100%); }
  .card--laptop .device-art { left: 590px; top: 0; width: 495px; height: 590px;
    background: linear-gradient(160deg, var(--sky-pale) 0%, var(--sky) 55%, var(--brand) 100%); }
  .card--laptop .person-name { left: 70px; top: 85px; }
  .card--laptop .person-role { left: 70px; top: 128px; }
  .card--laptop .company { left: 70px; top: 300px; }
  .card--laptop .address { left: 70px; top: 350px; }
  .card--laptop .phones { left: 70px; top: 440px; }
  .card--laptop .email { left: 70px; top: 528px; }
  .card--laptop .brand-name { left: 690px; top: 150px; }

  /* Card 2 */
  .card--waves .wave-art { left: 490px; top: 0; width: 595px; height: 762px;
    border-top-left-radius: 100% 100%;
    background: radial-gradient(circle at 100% 100%, var(--brand-deep) 0%, var(--brand) 35%, var(--sky) 65%, var(--sky-pale) 90%, rgba(255,255,255,0) 100%); }
  .card--waves .company { left: 60px; top: 105px; }
  .card--waves .address { left: 60px; top: 155px; }
  .card--waves .phones { left: 60px; top: 270px; }
  .card--waves .email { left: 60px; top: 380px; }
  .card--waves .logo-band { left: 0; top: 450px; width: 470px; height: 110px;
    background: linear-gradient(90deg, var(--sky-pale) 0%, var(--sky) 50%, rgba(255,255,255,0) 100%); }
  .card--waves .brand-name { left: 60px; top: 462px; }
  .card--waves .name-plate { left: 690px; top: 570px; width: 395px; height: 115px; background: var(--teal); padding: 16px 0 0 40px; }
  .card--waves .name-plate .person-name, .card--waves .name-plate .person-role { position: static; display: block; }

  /* Card 3 */
  .card--frame .frame-lines { left: 0; top: 0; width: 1085px; height: 572px; }
  .card--frame .wave-art { left: 0; top: 210px; width: 400px; height: 362px;
    border-top-right-radius: 100% 100%;
    background: radial-gradient(circle at 0% 100%, var(--brand) 0%, var(--sky) 40%, var(--sky-pale) 80%, rgba(255,255,255,0) 100%); }
  .card--frame .person-name { left: 40px; top: 95px; }
  .card--frame .person-role { left: 40px; top: 138px; }
  .card--frame .brand-name { left: 760px; top: 65px; }
  .card--frame .company { left: 440px; top: 245px; color: var(--ink); font-size: 36px; }
  .card--frame .address { left: 440px; top: 320px; color: var(--ink); }
  .card--frame .phones { left: 440px; top: 395px; color: var(--ink); }
  .card--frame .email-band { left: 340px; top: 505px; width: 745px; height: 52px;
    background: linear-gradient(90deg, rgba(255,255,255,0) 0%, var(--sky) 20%, var(--sky-pale) 100%); }
  .card--frame .email { left: 440px; top: 512px; color: var(--brand); }
</style>
</head>
<body>

<section class="card card--laptop">
  <div class="abs accent-band"></div>
  <div class="abs edge-glow"></div>
  <div class="abs device-art" role="img" aria-label="Illustration of an open laptop with a mobile phone beside it"></div>
  <div class="abs brand-name">Brevant</div>
  <div class="abs person-name">Dale Marwick</div>
  <div class="abs person-role">Managing Director</div>
  <div class="abs company">Brevant Electrical Products LTD</div>
  <div class="abs detail detail--caps address">7 Hapton Row<br>London, W4 9QD</div>
  <div class="abs detail detail--caps phones">Contact No:&nbsp;&nbsp;02085193604<br>Mobile:&nbsp;&nbsp;&nbsp;&nbsp;&nbsp;&nbsp;&nbsp;&nbsp;&nbsp;&nbsp;07814260537</div>
  <div class="abs detail detail--caps email">Email: info@brevant-goods.co.uk</div>
</section>

<section class="card card--waves">
  <div class="abs wave-art" role="img" aria-label="Concentric blue sound-wave arcs spreading from the lower right corner"></div>
  <div class="abs company">Brevant Electrical Products LTD</div>
  <div class="abs detail address">7 Hapton Row<br>London, W4 9QD</div>
  <div class="abs detail phones">Contact No: 02085193604<br>Mobile:&nbsp;&nbsp;&nbsp;&nbsp;&nbsp;&nbsp;&nbsp;&nbsp;&nbsp; 07814260537</div>
  <div class="abs detail email">Email: info@brevant-goods.co.uk</div>
  <div class="abs logo-band"></div>
  <div class="abs brand-name">Brevant</div>
  <div class="abs name-plate">
    <span class="person-name">Dale Marwick</span>
    <span class="person-role">Managing Director</span>
  </div>
</section>

<section class="card card--frame">
  <div class="abs wave-art" role="img" aria-label="Concentric light blue arcs spreading from the lower left corner"></div>
  <svg class="abs frame-lines" viewBox="0 0 1085 572" aria-hidden="true">
    <path d="M0 185 H560 Q610 185 620 140 L640 30 Q648 0 690 0" fill="none" stroke="var(--sky)" stroke-width="4"/>
    <path d="M330 300 Q360 292 420 292 H1085" fill="none" stroke="var(--sky)" stroke-width="6"/>
  </svg>
  <div class="abs person-name">Dale Marwick</div>
  <div class="abs person-role">Managing Director</div>
  <div class="abs brand-name">Brevant</div>
  <div class="abs company">Brevant Electrical Products LTD</div>
  <div class="abs detail address">7 Hapton Row, London, W4 9QD</div>
  <div class="abs detail phones">Contact No: 02085193604<br>Mobile: 07814260537</div>
  <div class="abs email-band"></div>
  <div class="abs detail email">Email: info@brevant-goods.co.uk</div>
</section>

</body>
</html>
```